Flyer Promoting Dental Benefit Program

I want to promote a dental benefit program to my patients that do not have dental insurance. This flyer would be posted in our waiting room and where people make payments. The goal would be to get those interested to request more information and enroll in the program. I have a card that will be issued that has a logo. Theflyer and card should feel congruent. I've uploaded a file with a copy of that card.
The plan costs $290/person. It includes 2 cleanings, exams, and x-rays. It also includes a 20% discount off of our standard fees. The plan or membership lasts for one year. It is only available to those without insurance. It is also important to let people know that this is not insurance (some kind of a disclaimer).
Updates
This plan is only available to patients at my office. The contact information is: Harborview Dental, 2718 West 4600 North Suite 209, Salt Lake City, Utah 84097. (801) 555-0187. info@harborviewdental.example. It is not necessary to include contact information as this flyer will be used as in-office promotion.
Target Market(s)
Those without dental insurance, but have resources to afford dental care.
Industry/Entity Type
Insurance
Look and feel
Each slider illustrates characteristics of the customer's brand and the style your logo design should communicate.

```html
<!DOCTYPE html>
<html lang="en">
<head>
<meta charset="utf-8">
<title>Brightkeep Care Plan Flyer</title>
<link href="https://fonts.googleapis.com/css2?family=Roboto+Condensed:wght@700&family=Open+Sans:wght@400;600;700&family=Crimson+Text:ital@1&display=swap" rel="stylesheet">
<style>
  :root {
    --green: #3f9b3d;
    --green-bright: #4cae45;
    --charcoal: #3a3a3a;
    --ink: #222222;
    --paper: #ffffff;
    --grey-text: #8a8a8a;
  }
  * { margin: 0; padding: 0; box-sizing: border-box; }
  html, body { width: 931px; height: 1200px; overflow: hidden; background: var(--paper); }
  .flyer { position: relative; width: 931px; height: 1200px; background: var(--paper); overflow: hidden; }

  .hero-photo {
    position: absolute; left: 0; top: 0; width: 931px; height: 590px;
    background:
      radial-gradient(ellipse at 20% 35%, #d9c8c0 0%, transparent 45%),
      radial-gradient(ellipse at 55% 45%, #e3cfc6 0%, transparent 40%),
      radial-gradient(ellipse at 85% 35%, #e6d2c8 0%, transparent 40%),
      linear-gradient(180deg, #8fa87c 0%, #b7b49a 40%, #c99aa8 75%, #b8a3c6 100%);
  }
  .hero-wave { position: absolute; left: 0; top: 420px; width: 931px; height: 200px; }

  .headline {
    position: absolute; left: 0; top: 645px; width: 382px;
    font-family: "Roboto Condensed", "Arial Narrow", sans-serif;
    font-weight: 700; font-size: 45px; line-height: 76px;
    color: var(--green); text-align: center;
  }

  .plan-name {
    position: absolute; left: 435px; top: 655px;
    display: flex; align-items: center; gap: 18px;
  }
  .plan-name .mark { width: 112px; height: 112px; border-radius: 50%; background: var(--green-bright); }
  .plan-name .name {
    font-family: "Open Sans", Arial, sans-serif; font-weight: 700;
    font-size: 40px; line-height: 1.05; color: var(--charcoal); width: 300px;
  }

  .discount-badge {
    position: absolute; left: 410px; top: 838px; width: 200px; height: 200px;
    border-radius: 50%; background: var(--charcoal); border: 9px solid var(--green-bright);
    color: var(--paper); text-align: center; padding-top: 30px;
  }
  .discount-badge .amount { font-family: "Open Sans", Arial, sans-serif; font-weight: 700; font-size: 29px; line-height: 32px; }
  .discount-badge .note { font-family: "Crimson Text", Georgia, serif; font-style: italic; font-size: 22px; line-height: 23px; margin-top: 4px; }

  .includes { position: absolute; left: 640px; top: 905px; font-family: "Open Sans", Arial, sans-serif; color: var(--ink); }
  .includes .lead { font-size: 25px; font-weight: 600; margin-bottom: 6px; }
  .includes ul { list-style: none; }
  .includes li { font-size: 26px; font-weight: 600; line-height: 37px; display: flex; align-items: center; }
  .includes li::before { content: ""; width: 16px; height: 16px; border-radius: 50%; background: var(--green-bright); margin-right: 12px; }

  .disclaimer {
    position: absolute; left: 410px; top: 1090px; width: 480px;
    font-family: "Open Sans", Arial, sans-serif; font-size: 13.5px; line-height: 20px; color: var(--ink);
  }
</style>
</head>
<body>
<main class="flyer">
  <div class="hero-photo" role="img" aria-label="Photograph of three smiling senior women standing together outdoors"></div>
  <svg class="hero-wave" viewBox="0 0 931 200" preserveAspectRatio="none" aria-hidden="true">
    <path d="M0 90 C 250 130, 600 60, 931 0 L931 200 L0 200 Z" fill="var(--green-bright)"/>
    <path d="M0 112 C 300 150, 620 95, 931 48 L931 200 L0 200 Z" fill="#ffffff"/>
    <path d="M0 120 C 300 170, 620 110, 931 62 C 620 125, 300 185, 0 150 Z" fill="#333333"/>
    <path d="M0 140 C 300 190, 620 125, 931 75 L931 200 L0 200 Z" fill="#ffffff"/>
  </svg>

  <h1 class="headline">Dental<br>benefit<br>program to<br>my patients<br>that do not<br>have dental<br>insurance</h1>

  <div class="plan-name">
    <span class="mark"></span>
    <span class="name">Brightkeep Care Plan</span>
  </div>

  <div class="discount-badge">
    <div class="amount">20%<br>discount</div>
    <div class="note">off our<br>standard<br>fees.</div>
  </div>

  <div class="includes">
    <p class="lead">it includes</p>
    <ul>
      <li>2 CLEANINGS</li>
      <li>EXAMS</li>
      <li>X-RAYS</li>
    </ul>
  </div>

  <p class="disclaimer">The plan or membership lasts for one year. It is only available to those without insurance. It is also important to let people know that this is not insurance (some kind of a disclaimer).</p>
</main>
</body>
</html>
```